Description of Adventure Certificate:
We require a certificate, that will be awarded to winners of competitions and offered to fundraising organisations for a $ value or type of event service we provide.
The certificate will be professionally printed on thick high-quality paper.
Design concept: Adventurous outer border, and exciting theme.
Title: Adventure Certificate (adventurous font)
Content: "Bringing the Thrill of Adventure to you"
Awarded To:..........................................
From:....................................................
Amount / Event: ...................................
Redemption Location:...........................
Expires:.................................................
Events listed near the base of certificate: Community events, Sports celebrations, Team building, School activities, Festivals, Vacation Care, EXPO's, Trade Shows.
Contact: M: 0418 527 394
E: info@quillmarsh.com.au
Images: Quill Marsh Logo
Adventure Certificate image
Carabiner

```html
<!DOCTYPE html>
<html lang="en">
<head>
<meta charset="utf-8">
<title>Adventure Certificate – Quill Marsh</title>
<link href="https://fonts.googleapis.com/css2?family=Oswald:wght@300;400;500;700&family=Stardos+Stencil:wght@700&display=swap" rel="stylesheet">
<style>
  :root{
    --paper:#ececec;
    --paper-edge:#e2e2e2;
    --ink:#1c1c1c;
    --muted:#4a4a4a;
    --accent:#e8442a;
    --accent-light:#f0603f;
    --accent-dark:#d8381f;
    --torn:#b8a78f;
    --white:#ffffff;
  }
  *{box-sizing:border-box;margin:0;padding:0}
  html,body{width:1200px;height:883px;overflow:hidden;background:#d9d9d9}
  .certificate{
    position:relative;width:1200px;height:883px;overflow:hidden;
    background:radial-gradient(ellipse at 55% 60%, #f3f3f3 0%, var(--paper) 55%, var(--paper-edge) 100%);
    font-family:"Oswald",sans-serif;color:var(--ink);
  }
  .hero-photo{
    position:absolute;left:0;top:0;width:1200px;height:358px;
    background:
      linear-gradient(90deg, rgba(60,80,110,.85) 0%, rgba(60,80,110,0) 22%, rgba(60,80,110,0) 80%, rgba(150,170,195,.9) 100%),
      linear-gradient(180deg, #9a3a28 0%, #b04a33 50%, #8c3322 100%);
    clip-path:polygon(0 0,100% 0,100% 97%,92% 99%,84% 96%,75% 98.5%,66% 96.5%,57% 99%,48% 97%,39% 99.5%,30% 96.5%,21% 98.5%,12% 96%,4% 99%,0 97%);
  }
  .torn-edge{
    position:absolute;left:0;top:347px;width:1200px;height:14px;
    background:linear-gradient(180deg,var(--torn),rgba(184,167,143,0));
  }
  .carabiner{
    position:absolute;left:46px;top:330px;width:74px;height:112px;
    border:9px solid #c42a2a;border-radius:38px;background:transparent;
  }
  .title{position:absolute;left:0;top:372px;width:1200px;height:80px}
  .title text{font-family:"Stardos Stencil",sans-serif;font-weight:700;font-size:66px;fill:var(--ink)}
  .title-rule{
    position:absolute;left:149px;top:459px;width:894px;height:3px;
    background:linear-gradient(90deg,rgba(28,28,28,0),var(--ink) 8%,var(--ink) 92%,rgba(28,28,28,0));
  }
  .tagline{
    position:absolute;left:0;top:484px;width:1200px;text-align:center;
    font-weight:500;font-size:31px;letter-spacing:.3px;color:var(--accent);text-transform:uppercase;
  }
  .fields{position:absolute;left:103px;top:548px;width:981px;list-style:none}
  .field{display:flex;align-items:baseline;height:39.5px;font-size:27px;font-weight:400;letter-spacing:-.3px}
  .field-line{flex:1;border-bottom:2px dotted var(--ink);margin-left:3px;transform:translateY(-5px)}
  .field--short{width:497px}
  .services{
    position:absolute;left:103px;top:756px;font-size:17px;font-weight:300;color:var(--muted);letter-spacing:-.2px;
  }
  .contact-band{
    position:absolute;left:0;top:801px;width:1200px;height:82px;
    background:linear-gradient(100deg,var(--accent-dark) 0%,var(--accent) 45%,var(--accent-light) 70%,var(--accent) 100%);
  }
  .contact{
    position:absolute;top:823px;display:flex;align-items:center;gap:12px;
    color:var(--white);font-size:27px;font-weight:400;letter-spacing:-.3px;
  }
  .contact--phone{left:112px}
  .contact--email{left:346px}
  .contact svg{width:26px;height:26px}
  .brand{
    position:absolute;left:880px;top:748px;display:flex;align-items:center;gap:12px;
  }
  .brand-mark{width:58px;height:58px;border-radius:50%;background:var(--accent)}
  .brand-name{font-size:40px;font-weight:700;color:var(--ink);text-transform:uppercase;letter-spacing:.5px}
</style>
</head>
<body>
<main class="certificate">
  <div class="hero-photo" role="img" aria-label="Photo of two children climbing a red rock-climbing wall against a blue sky, with a branded banner on the left"></div>
  <div class="torn-edge"></div>
  <div class="carabiner" role="img" aria-label="Red climbing carabiner"></div>

  <svg class="title" viewBox="0 0 1200 80" aria-label="Adventure Certificate">
    <text x="600" y="64" text-anchor="middle" textLength="810" lengthAdjust="spacingAndGlyphs">ADVENTURE CERTIFICATE</text>
  </svg>
  <div class="title-rule"></div>

  <p class="tagline">Bringing the thrill of adventure to you</p>

  <ul class="fields">
    <li class="field">Awarded To:<span class="field-line"></span></li>
    <li class="field">From:<span class="field-line"></span></li>
    <li class="field">Amount / Event:<span class="field-line"></span></li>
    <li class="field">Redemption Location:<span class="field-line"></span></li>
    <li class="field field--short">Expires:<span class="field-line"></span></li>
  </ul>

  <p class="services">Community events, Sports celebrations, Team building, School activities, Festivals, Vacation Care, EXPO's, Trade Shows.</p>

  <div class="contact-band"></div>
  <div class="contact contact--phone">
    <svg viewBox="0 0 26 26" aria-hidden="true"><rect width="26" height="26" rx="4" fill="#fff"/><path d="M8 6c1 0 2 2.5 2 3.2S8.8 10.6 9 11.3c.6 2 3.4 4.8 5.4 5.4.7.2 1.4-1 2.1-1s3.2 1 3.2 2c0 1.5-1.6 2.6-3 2.4C11 19.3 6.7 15 6 9.3 5.8 7.7 6.8 6 8 6z" fill="var(--accent)"/></svg>
    <span>0418 527 394</span>
  </div>
  <div class="contact contact--email">
    <svg viewBox="0 0 26 26" aria-hidden="true"><rect width="26" height="26" rx="4" fill="#fff"/><rect x="5" y="7.5" width="16" height="11" rx="1" fill="none" stroke="var(--accent)" stroke-width="1.8"/><path d="M5.5 8.2 13 14l7.5-5.8M5.5 17.8l5.5-5M20.5 17.8l-5.5-5" fill="none" stroke="var(--accent)" stroke-width="1.6"/></svg>
    <span>info@quillmarsh.com.au</span>
  </div>

  <div class="brand">
    <span class="brand-mark"></span>
    <span class="brand-name">Quill Marsh</span>
  </div>
</main>
</body>
</html>
```